Business cards real estate company

We need a design for a business card. It is a company that specializes in real estate sales. There should be space for a photo of the respective employee as well as the website and telephone number on it. Design should be noble, innovative.

Contact Information for Business Card

Website, Name, Position, Telefonnummer

Requirements
Must have
• Photo, logo

```html
<!DOCTYPE html>
<html lang="en">
<head>
<meta charset="utf-8">
<title>Greenova Business Card</title>
<link href="https://fonts.googleapis.com/css2?family=Poppins:wght@400;500;600;700&display=swap" rel="stylesheet">
<style>
  :root {
    --page-bg: #e9ebe6;
    --lime: #b6d433;
    --green: #6cb842;
    --green-dark: #5aa936;
    --ink: #1d1d1d;
    --white: #ffffff;
    --photo-warm: #8a5a3a;
    --photo-cool: #3e5a8a;
  }
  * { box-sizing: border-box; margin: 0; padding: 0; }
  html, body { width: 1200px; height: 900px; overflow: hidden; }
  body {
    background: var(--page-bg);
    font-family: "Poppins", sans-serif;
    position: relative;
  }
  .card {
    position: absolute;
    left: 280px;
    width: 640px;
    height: 366px;
    border-radius: 24px;
    overflow: hidden;
    box-shadow: 0 10px 30px rgba(0,0,0,0.18);
  }
  /* Back side */
  .card-back {
    top: 50px;
    background: linear-gradient(200deg, var(--green) 0%, #93c63c 55%, var(--lime) 100%);
  }
  .card-back .brand {
    position: absolute;
    top: 140px;
    left: 0; right: 0;
    text-align: center;
    color: var(--white);
    font-weight: 700;
    font-size: 62px;
    letter-spacing: 1px;
  }
  .card-back .web {
    position: absolute;
    right: 60px;
    bottom: 36px;
    color: var(--white);
    font-size: 15px;
    font-weight: 500;
    letter-spacing: 0.5px;
  }
  /* Front side */
  .card-front {
    top: 470px;
    background: var(--white);
  }
  .photo-ring {
    position: absolute;
    left: 70px;
    top: 78px;
    width: 214px;
    height: 214px;
    border-radius: 50%;
    background: linear-gradient(135deg, var(--green), var(--lime));
    padding: 9px;
  }
  .photo {
    width: 100%;
    height: 100%;
    border-radius: 50%;
    border: 5px solid var(--white);
    background: radial-gradient(circle at 35% 30%, var(--photo-warm) 0%, #5a3a2a 50%, var(--photo-cool) 100%);
  }
  .details {
    position: absolute;
    left: 330px;
    top: 62px;
  }
  .details .brand {
    color: var(--green);
    font-weight: 700;
    font-size: 46px;
    line-height: 1;
    letter-spacing: 0.5px;
  }
  .details .name {
    margin-top: 18px;
    color: var(--ink);
    font-weight: 600;
    font-size: 22px;
    line-height: 1.1;
  }
  .details .role {
    color: var(--green);
    font-weight: 400;
    font-size: 15px;
    letter-spacing: 0.5px;
  }
  .contacts {
    list-style: none;
    margin-top: 22px;
  }
  .contacts li {
    display: flex;
    align-items: center;
    gap: 12px;
    color: var(--ink);
    font-size: 15px;
    margin-bottom: 10px;
  }
  .contacts .icon {
    width: 24px;
    height: 24px;
    flex: none;
  }
</style>
</head>
<body>

<section class="card card-back">
  <div class="brand">Greenova</div>
  <div class="web">www.greenova-homes.com</div>
</section>

<section class="card card-front">
  <div class="photo-ring">
    <div class="photo" role="img" aria-label="Portrait photo of the employee"></div>
  </div>

  <div class="details">
    <div class="brand">Greenova</div>
    <div class="name">Jonas Weller</div>
    <div class="role">Managing Director</div>

    <ul class="contacts">
      <li>
        <svg class="icon" viewBox="0 0 24 24" aria-hidden="true">
          <circle cx="12" cy="12" r="12" fill="#6cb842"/>
          <path d="M8.2 6.5c.4-.3 1-.3 1.3.1l1.3 1.8c.3.4.2.9-.1 1.2l-.8.7c.6 1.3 1.6 2.4 2.9 3.1l.7-.8c.3-.4.9-.4 1.2-.1l1.8 1.3c.4.3.4.9.1 1.3l-.9 1c-.5.5-1.3.7-2 .4-3.1-1.3-5.4-3.7-6.6-6.8-.3-.7-.1-1.5.4-2z" fill="#fff"/>
        </svg>
        0815-3921-4470
      </li>
      <li>
        <svg class="icon" viewBox="0 0 24 24" aria-hidden="true">
          <circle cx="12" cy="12" r="12" fill="#6cb842"/>
          <rect x="6" y="8" width="12" height="8.5" rx="1" fill="#fff"/>
          <path d="M6.5 8.6l5.5 4.2 5.5-4.2" fill="none" stroke="#6cb842" stroke-width="1.2"/>
        </svg>
        info@greenova-homes.com
      </li>
      <li>
        <svg class="icon" viewBox="0 0 24 24" aria-hidden="true">
          <circle cx="12" cy="12" r="12" fill="#6cb842"/>
          <g fill="none" stroke="#fff" stroke-width="1.2">
            <circle cx="12" cy="12" r="6"/>
            <ellipse cx="12" cy="12" rx="2.6" ry="6"/>
            <path d="M6 12h12M7 9h10M7 15h10"/>
          </g>
        </svg>
        www.greenova-homes.com
      </li>
    </ul>
  </div>
</section>

</body>
</html>
```